Help design website for "Civic Lantern Advisors" to advance the common good

Here is the Google doc link that lays out the design:

https://files.quorvinex.com/page/d/7TxRmWqa2ZbLkc9YhVnE4PdUs0GfJo3XiKv8Nt5Ry6Mw/edit?usp=sharing

Here is the Google drive folder with the logos and photos: https://store.quorvinex.com/open?id=4Kp9XmRtLwQ2bVnZc83Hs6YdJe0Fu

The testimonials are being gathered and will be shared by Friday, 1/4.

The winner will also have to migrate the coding files to my hosting site.

Thank you for your help! Looking forward to seeing your designs.

Target Market(s)

Prospective clients

Industry/Entity Type

Non Profit

Coding

Coded - Design and coding required

Number of Pages Required

5+ page

Requirements
Must have
• Noted in the Google doc regarding layout.
Nice to have

```html
<!DOCTYPE html>
<html lang="en">
<head>
<meta charset="utf-8">
<title>Civic Lantern Advisors</title>
<link rel="stylesheet" href="https://fonts.googleapis.com/css2?family=Montserrat:wght@400;500;600;700&family=Lato:wght@300;400;700&display=swap">
<style>
  :root {
    --backdrop: #6b6767;
    --ink-dark: #2a2d36;
    --brand-blue: #4e9fd6;
    --link-blue: #3d8fd0;
    --sky-light: #e8f3fb;
    --sky-mid: #6fb3e3;
    --sky-deep: #1f5f9a;
    --band-grey: #dcdde0;
    --pattern-grey: #e6e8ec;
    --white: #ffffff;
    --text-body: #333333;
  }
  * { box-sizing: border-box; margin: 0; padding: 0; }
  html, body { width: 1200px; height: 2191px; overflow: hidden; }
  body { position: relative; background: var(--backdrop); font-family: "Lato", sans-serif; }
  .page { position: absolute; left: 96px; top: 56px; width: 985px; height: 2080px; background: var(--white); box-shadow: 0 4px 14px rgba(0,0,0,.35); overflow: hidden; }
  .abs { position: absolute; }

  .site-nav { left: 0; top: 0; width: 985px; height: 82px; background: var(--ink-dark); }
  .site-nav::after { content: ""; position: absolute; left: 0; bottom: -6px; width: 100%; height: 6px; background: var(--brand-blue); }
  .nav-links { left: 89px; top: 46px; transform: translateY(-50%); display: flex; font-family: "Montserrat", sans-serif; font-weight: 600; font-size: 11.5px; color: var(--white); }
  .nav-links span { padding: 0 14px; border-left: 1px solid #7d8aa0; line-height: 14px; }
  .nav-links span:first-child { border-left: 0; padding-left: 0; color: var(--brand-blue); }
  .brand { left: 758px; top: 22px; display: flex; align-items: center; gap: 9px; }
  .brand-mark { width: 26px; height: 26px; background: var(--brand-blue); }
  .brand-name { font-family: "Montserrat", sans-serif; font-weight: 500; font-size: 10px; letter-spacing: 2px; color: var(--white); line-height: 12px; width: 110px; }

  .hero { left: 0; top: 88px; width: 985px; height: 442px; background: linear-gradient(160deg, var(--sky-light) 0%, var(--sky-mid) 45%, var(--sky-deep) 100%); }
  .hero-title { left: 0; width: 985px; top: 250px; text-align: center; font-family: "Montserrat", sans-serif; font-weight: 700; font-size: 53px; color: var(--ink-dark); line-height: 1; }
  .hero-sub { left: 0; width: 985px; top: 318px; text-align: center; font-family: "Montserrat", sans-serif; font-weight: 500; font-size: 23px; color: var(--ink-dark); }
  .hero-button { left: 402px; top: 362px; width: 180px; height: 40px; border: 1.5px solid var(--link-blue); border-radius: 3px; background: rgba(255,255,255,.35); font-family: "Montserrat", sans-serif; font-weight: 500; font-size: 18px; color: var(--link-blue); display: flex; align-items: center; justify-content: center; }
  .hero-arrow { top: 323px; width: 14px; height: 24px; }

  .section-band { height: 30px; background: var(--pattern-grey); }
  .section-icon { width: 60px; height: 60px; border: 2px solid var(--brand-blue); border-radius: 50%; background: var(--white); display: flex; align-items: center; justify-content: center; }
  .section-title { left: 0; width: 985px; text-align: center; font-family: "Montserrat", sans-serif; font-weight: 500; font-size: 27px; color: var(--ink-dark); letter-spacing: .5px; }

  .about-lead { left: 134px; top: 676px; width: 716px; text-align: center; font-family: "Lato", sans-serif; font-weight: 700; font-size: 21px; line-height: 34px; color: var(--brand-blue); }
  .founder-photo { left: 115px; top: 792px; width: 232px; height: 232px; border-radius: 50%; border: 2px solid var(--brand-blue); background: radial-gradient(circle at 50% 40%, #8a7a70 0%, #4a4240 55%, #b9b4ae 100%); }
  .founder-bio { left: 399px; top: 763px; width: 453px; font-family: "Lato", sans-serif; font-weight: 400; font-size: 10.6px; line-height: 17.5px; color: var(--text-body); text-align: justify; }
  .founder-bio p + p { margin-top: 16px; }

  .history-band { left: 0; top: 1267px; width: 985px; height: 586px; background: var(--band-grey); }
  .client-card { width: 214px; height: 247px; background: var(--white); border-bottom: 9px solid var(--brand-blue); }
  .client-mark { position: absolute; left: 14px; right: 14px; top: 40px; height: 100px; display: flex; align-items: center; justify-content: center; gap: 8px; font-family: "Montserrat", sans-serif; font-weight: 700; font-size: 15px; line-height: 19px; color: var(--ink-dark); text-align: center; }
  .client-mark i { flex: none; width: 22px; height: 22px; border-radius: 50%; background: var(--brand-blue); }
  .client-name { position: absolute; left: 12px; right: 12px; top: 184px; text-align: center; font-family: "Lato", sans-serif; font-size: 12.5px; line-height: 16px; color: var(--link-blue); }

  .social-band { left: 0; top: 1914px; width: 985px; height: 110px; background: var(--brand-blue); }
  .social-dot { top: 1931px; width: 36px; height: 36px; border: 2px solid var(--white); border-radius: 50%; }
  .site-footer { left: 0; top: 2024px; width: 985px; height: 56px; background: var(--ink-dark); display: flex; align-items: center; justify-content: center; font-family: "Montserrat", sans-serif; font-weight: 500; font-size: 13px; color: var(--white); letter-spacing: .3px; }
</style>
</head>
<body>
<div class="page">

  <header class="site-nav abs">
    <nav class="nav-links abs">
      <span>ABOUT</span><span>SERVICES &amp; TESTIMONIALS</span><span>MEDIA &amp; IMPACT</span><span>CONTACT</span>
    </nav>
    <div class="brand abs">
      <div class="brand-mark"></div>
      <div class="brand-name">CIVIC LANTERN ADVISORS</div>
    </div>
  </header>

  <section class="hero abs" role="img" aria-label="Photo of glass skyscrapers rising into a bright blue sky with clouds"></section>
  <svg class="hero-arrow abs" style="left:44px" viewBox="0 0 14 24"><polyline points="12,2 2,12 12,22" fill="none" stroke="#ffffff" stroke-width="2"/></svg>
  <svg class="hero-arrow abs" style="left:926px" viewBox="0 0 14 24"><polyline points="2,2 12,12 2,22" fill="none" stroke="#ffffff" stroke-width="2"/></svg>
  <h1 class="hero-title abs">We’ll get it done</h1>
  <p class="hero-sub abs">Our reputation is the proof</p>
  <div class="hero-button abs">MORE</div>

  <div class="section-band abs" role="img" aria-label="Decorative chevron pattern" style="left:0;top:564px;width:430px"></div>
  <div class="section-band abs" role="img" aria-label="Decorative chevron pattern" style="left:556px;top:564px;width:429px"></div>
  <div class="section-icon abs" style="left:463px;top:549px">
    <svg width="34" height="30" viewBox="0 0 34 30" fill="#4e9fd6">
      <circle cx="9" cy="9" r="4.5"/><circle cx="25" cy="9" r="4.5"/><circle cx="17" cy="7" r="6"/>
      <path d="M1 24c0-5 4-8 8-8s8 3 8 8z"/><path d="M17 24c0-5 4-8 8-8s8 3 8 8z"/><path d="M7 27c0-6 4.5-10 10-10s10 4 10 10z"/>
    </svg>
  </div>
  <h2 class="section-title abs" style="top:611px">ABOUT</h2>

  <p class="about-lead abs">Civic Lantern Advisors supports nonprofit organizations and educational institutions to carry out their missions to benefit the wider community.</p>

  <div class="founder-photo abs" role="img" aria-label="Portrait photo of the founder"></div>
  <div class="founder-bio abs">
    <p>Founder Mara Ellison is an educator with a 22-year record of demonstrated achievement and leadership roles in nonprofits and educational institutions. Most recently, she served as Associate Dean of Students in the University and Director of the Campus Civic Service Hub at Lakeshore University. Mara has designed, implemented, and evaluated community-based learning and leadership training programs that have attained positive outcomes documented by survey results, recognition by outside agencies, and grants awarded for new initiatives and expansions. She has also significantly and consistently increased the number of program applicants, volunteers, and community partnerships through innovative programming, improved reputation, targeted recruitment, marketing and communications.</p>
    <p>Mara is a native Chicagoan and has also lived in Tokyo, Boston, San Francisco, and Washington, DC. Mara received her bachelor of arts from Fenwick College in Millbrook, MN and her masters in education from Ashgrove University in Easton, MA.</p>
  </div>

  <div class="section-band abs" role="img" aria-label="Decorative chevron pattern" style="left:0;top:1160px;width:430px"></div>
  <div class="section-band abs" role="img" aria-label="Decorative chevron pattern" style="left:556px;top:1160px;width:429px"></div>
  <div class="section-icon abs" style="left:463px;top:1144px">
    <svg width="32" height="28" viewBox="0 0 32 28" fill="#4e9fd6">
      <path d="M11 4V2h10v2h-2V4h-6z"/><rect x="11" y="1" width="10" height="3" rx="1" fill="none" stroke="#4e9fd6" stroke-width="2"/>
      <rect x="1" y="5" width="30" height="21" rx="3"/><rect x="1" y="13" width="30" height="2" fill="#ffffff"/><rect x="14" y="11" width="4" height="6" fill="#ffffff"/>
    </svg>
  </div>
  <h2 class="section-title abs" style="top:1210px">WORK HISTORY</h2>

  <section class="history-band abs"></section>
  <div class="client-card abs" style="left:135px;top:1295px"><div class="client-mark"><i></i>Campus Civic Service Hub</div><div class="client-name">Campus Civic Service Hub</div></div>
  <div class="client-card abs" style="left:386px;top:1295px"><div class="client-mark"><i></i>Meridian</div><div class="client-name">Meridian Center for Civic Leadership</div></div>
  <div class="client-card abs" style="left:637px;top:1295px"><div class="client-mark">Bayline Public Schools</div><div class="client-name">Bayline Public Schools</div></div>
  <div class="client-card abs" style="left:135px;top:1578px"><div class="client-mark">Neighbor Scholars</div><div class="client-name">Neighbor Scholars</div></div>
  <div class="client-card abs" style="left:386px;top:1578px"><div class="client-mark"><i></i>ServeNation Fellows</div><div class="client-name">ServeNation Fellows</div></div>
  <div class="client-card abs" style="left:637px;top:1578px"><div class="client-mark">Pacific Exchange</div><div class="client-name">Pacific Exchange Teaching Programme</div></div>

  <section class="social-band abs"></section>
  <div class="social-dot abs" style="left:367px"></div>
  <div class="social-dot abs" style="left:438px"></div>
  <div class="social-dot abs" style="left:512px"></div>
  <div class="social-dot abs" style="left:583px"></div>

  <footer class="site-footer abs">CIVIC LANTERN ADVISORS © 2019</footer>
</div>
</body>
</html>
```